Business cards and stationery for Montessori school
Ridgeway Hollow Montessori
Business cards and stationery for Montessori school - Education
Creative Brief
Professional
Harpreet Malvik
Director
26415 48th Ave NE Kenmore WA 98094
425-613-PLAY (7529)
hmalvik@ridgewayhollowschool.org
www.ridgewayhollowschool.org
Need design for a good business card and stationary including letter heads and envelopes. Letter head should not have cell phone no. and email address should be info@ridgewayhollowschool.org.
Either enlarged logo or logo with school name and mission "Learning, Striving, Ascending".

```html
<!DOCTYPE html>
<html lang="en">
<head>
<meta charset="utf-8">
<title>Ridgeway Hollow Montessori — Business Card</title>
<link rel="stylesheet" href="https://fonts.googleapis.com/css2?family=Open+Sans:wght@400;600;700;800&display=swap">
<style>
  :root {
    --backdrop: #ecebe8;
    --card-white: #ffffff;
    --panel-teal: #1d4a5b;
    --stripe-grey: #a7bcc6;
    --ink-navy: #1f3f5a;
    --logo-dot: #2f8fa3;
    --text-light: #ffffff;
  }
  * { margin: 0; padding: 0; box-sizing: border-box; }
  html, body {
    width: 1200px;
    height: 958px;
    overflow: hidden;
    background: var(--backdrop);
    font-family: "Open Sans", Arial, sans-serif;
  }
  .card {
    position: absolute;
    left: 90px;
    top: 187px;
    width: 1020px;
    height: 583px;
    background: var(--card-white);
    overflow: hidden;
    box-shadow: 0 10px 30px rgba(0,0,0,0.18);
  }
  .card-shapes {
    position: absolute;
    inset: 0;
    width: 100%;
    height: 100%;
  }
  .brand {
    position: absolute;
    left: 50px;
    top: 170px;
    width: 400px;
    text-align: center;
  }
  .brand-dot {
    display: block;
    width: 120px;
    height: 120px;
    margin: 0 auto 26px;
    border-radius: 50%;
    background: var(--logo-dot);
  }
  .brand-name {
    font-weight: 800;
    font-size: 30px;
    line-height: 1.15;
    letter-spacing: 0.5px;
    color: var(--ink-navy);
    text-transform: uppercase;
  }
  .contact {
    position: absolute;
    right: 60px;
    top: 56px;
    text-align: right;
    color: var(--text-light);
  }
  .contact-name {
    font-weight: 700;
    font-size: 30px;
    line-height: 1.2;
  }
  .contact-title {
    font-weight: 400;
    font-size: 27px;
    line-height: 1.25;
    margin-bottom: 58px;
  }
  .contact-line {
    display: flex;
    justify-content: flex-end;
    align-items: center;
    gap: 10px;
    font-size: 24px;
    line-height: 1.55;
    white-space: nowrap;
  }
  .contact-icon {
    width: 22px;
    height: 22px;
    fill: var(--text-light);
    flex: none;
  }
</style>
</head>
<body>
  <div class="card">
    <svg class="card-shapes" viewBox="0 0 1020 583" aria-hidden="true">
      <path d="M470 0 C385 140 395 420 525 583 L600 583 C470 430 470 120 560 0 Z" fill="var(--stripe-grey)"/>
      <path d="M560 0 C470 120 470 430 600 583 L1020 583 L1020 0 Z" fill="var(--panel-teal)"/>
      <path d="M560 0 C470 120 470 430 600 583" fill="none" stroke="var(--card-white)" stroke-width="14"/>
    </svg>

    <div class="brand">
      <span class="brand-dot"></span>
      <p class="brand-name">Ridgeway Hollow<br>Montessori</p>
    </div>

    <div class="contact">
      <p class="contact-name">Corwin Ashby-Lane</p>
      <p class="contact-title">Consultant</p>
      <p class="contact-line">26415 48th Ave NE</p>
      <p class="contact-line">Kenmore WA 98094</p>
      <p class="contact-line">425-613-PLAY (7529)
        <svg class="contact-icon" viewBox="0 0 24 24"><path d="M6.6 10.8a15.1 15.1 0 0 0 6.6 6.6l2.2-2.2a1 1 0 0 1 1-.25 11.4 11.4 0 0 0 3.6.57 1 1 0 0 1 1 1V20a1 1 0 0 1-1 1A17 17 0 0 1 3 4a1 1 0 0 1 1-1h3.5a1 1 0 0 1 1 1 11.4 11.4 0 0 0 .57 3.6 1 1 0 0 1-.25 1z"/></svg>
      </p>
      <p class="contact-line">425-613-2084
        <svg class="contact-icon" viewBox="0 0 24 24"><path d="M7 2h10a2 2 0 0 1 2 2v16a2 2 0 0 1-2 2H7a2 2 0 0 1-2-2V4a2 2 0 0 1 2-2zm0 3v12h10V5zm5 13.2a1.2 1.2 0 1 0 0 2.4 1.2 1.2 0 0 0 0-2.4z"/></svg>
      </p>
      <p class="contact-line">cashby@ridgewayhollowschool.org
        <svg class="contact-icon" viewBox="0 0 24 24"><path d="M3 5h18a1 1 0 0 1 1 1v12a1 1 0 0 1-1 1H3a1 1 0 0 1-1-1V6a1 1 0 0 1 1-1zm1 2.2V17h16V7.2l-8 5.6z"/></svg>
      </p>
      <p class="contact-line">www.ridgewayhollowschool.org</p>
    </div>
  </div>
</body>
</html>
```